Redesign for existing homepage

We would like a redesign for our websites 2 column homepage
We provide engine repair and reconditioning services
We would like a cleaner, modern site that works well with our logo colors
Please see the attached brief for more info
Target Market(s)
25 - 45
Industry/Entity Type
Cleaner
Requirements
Must have
- Google Fonts

```html
<!DOCTYPE html>
<html lang="en">
<head>
<meta charset="utf-8">
<title>Harlow Brandt Engine Reconditioners</title>
<link href="https://fonts.googleapis.com/css2?family=Questrial&family=Open+Sans:wght@400;600;700&display=swap" rel="stylesheet">
<style>
:root{
  --blue:#3d70b9;
  --blue-text:#3b73bf;
  --gold:#d9a52c;
  --charcoal:#3b3b3b;
  --header:#2b2b2b;
  --nav:#3a3a3a;
  --nav-line:#555;
  --ink:#333;
  --white:#fff;
  --footer:#222;
}
*{box-sizing:border-box;margin:0;padding:0}
html,body{width:706px;height:1200px;overflow:hidden}
body{position:relative;background:var(--white);font-family:"Open Sans",Arial,sans-serif;color:var(--ink)}
.topbar{position:absolute;left:0;top:0;width:706px;height:27px;background:var(--blue);color:var(--white);font-size:12px}
.topbar__call{position:absolute;right:143px;top:6px}
.topbar__email{position:absolute;left:584px;top:0;width:90px;height:27px;background:var(--gold);font-size:10px;font-weight:700;display:flex;align-items:center;justify-content:center;gap:6px}
.site-header{position:absolute;left:0;top:27px;width:706px;height:133px;background:var(--header)}
.brand{position:absolute;left:33px;top:36px;display:flex;align-items:center;gap:10px;color:var(--white);font-family:"Open Sans",sans-serif;font-weight:700;font-size:26px;letter-spacing:.5px}
.brand__dot{width:18px;height:18px;border-radius:50%;background:var(--white)}
.site-header__tag{position:absolute;left:31px;top:94px;color:var(--white);font-size:11px;letter-spacing:.2px}
.nav{position:absolute;left:0;top:160px;width:706px;height:35px;background:var(--nav);display:flex;padding-left:32px}
.nav__item{color:var(--white);font-size:9.5px;padding:0 9px;display:flex;align-items:center;border-left:1px solid var(--nav-line)}
.nav__item:last-child{border-right:1px solid var(--nav-line)}
.hero{position:absolute;left:0;top:195px;width:706px;height:135px;background:linear-gradient(90deg,#eaeaea 0%,#e3e3e3 35%,#b8b3ad 55%,#7a6a5c 75%,#9a9793 100%)}
.hero__title{position:absolute;left:31px;top:27px;font-family:"Questrial",sans-serif;font-size:22px;line-height:27px;color:#333}
.hero__sub{position:absolute;left:33px;top:88px;font-family:"Questrial",sans-serif;font-size:13px;color:#333}
.service{position:absolute;left:32px;width:423px;border-left:4px solid var(--blue)}
.service__body{padding-left:14px;width:258px}
.service__title{font-family:"Questrial",sans-serif;font-weight:400;font-size:14px;line-height:16.5px;color:var(--blue-text);margin-top:-1px;margin-bottom:6px}
.service__text{font-size:9px;line-height:11.5px;color:#333;margin-bottom:7px}
.btn{display:inline-flex;align-items:center;justify-content:center;width:102px;height:32px;font-size:9px;font-weight:700}
.btn--blue{background:var(--blue);color:var(--white)}
.btn--gold{background:var(--gold);color:var(--white)}
.btn--white{background:var(--white);color:var(--blue)}
.service .btn{margin-top:7px}
.service__photo{position:absolute;left:276px;top:0;width:146px;height:140px;border-radius:5px}
.sidebar{position:absolute;left:474px;top:354px;width:200px}
.cta{padding:13px 19px 0;color:var(--white)}
.cta--dark{background:var(--charcoal)}
.cta--blue{background:var(--blue)}
.cta__title{font-family:"Questrial",sans-serif;font-weight:400;font-size:14px;line-height:16.5px;margin-bottom:7px}
.cta__text{font-size:9px;line-height:11.5px;margin-bottom:12px}
.partners{position:absolute;left:0;top:1093px;width:706px;height:67px;background:var(--blue);color:var(--white);font-size:9px;font-weight:700;line-height:12px}
.partners__badge-a{position:absolute;left:33px;top:16px;width:60px;height:36px;border-radius:50%;background:#1e1e1e}
.partners__text-a{position:absolute;left:103px;top:20px;width:240px}
.partners__badge-b{position:absolute;left:363px;top:14px;width:29px;height:33px;background:#e8d21e}
.partners__text-b{position:absolute;left:402px;top:20px}
.site-footer{position:absolute;left:0;top:1160px;width:706px;height:40px;background:var(--footer);color:#ddd;font-size:9px;padding:15px 32px}
</style>
</head>
<body>
<div class="topbar">
  <span class="topbar__call">Call us to get your engine running perfectly! Eastbay: (04) 555 0137</span>
  <span class="topbar__email">Email Us
    <svg width="11" height="8" viewBox="0 0 11 8"><rect x="0.5" y="0.5" width="10" height="7" fill="#fff"/><path d="M0.5 0.5 5.5 4.5 10.5 0.5" fill="none" stroke="#d9a52c" stroke-width="1"/></svg>
  </span>
</div>

<header class="site-header">
  <div class="brand"><span class="brand__dot"></span>Harlow Brandt</div>
  <p class="site-header__tag">ENGINE REPAIRS AND RECONDITIONING SPECIALISTS</p>
</header>

<nav class="nav">
  <span class="nav__item">Home</span>
  <span class="nav__item">About Us</span>
  <span class="nav__item">Private Vehicle Service &amp; Repair</span>
  <span class="nav__item">Trade Customers</span>
  <span class="nav__item">Race &amp; Classic Car Engines</span>
  <span class="nav__item">Make an Enquiry</span>
  <span class="nav__item">Contact Us</span>
</nav>

<section class="hero" role="img" aria-label="Close-up of engine gears and pulleys">
  <h1 class="hero__title" style="font-weight:400">Specialist engine repair<br>&amp; reconditioning</h1>
  <p class="hero__sub">To have your car running at its best</p>
</section>

<article class="service" style="top:353px;height:160px">
  <div class="service__body">
    <h2 class="service__title">Do you have a personal or family car that needs a repair?</h2>
    <p class="service__text">Don't put up with your vehicle making irregular noises or breaking down! You can contact us to pinpoint the problem with your vehicle and have it running smoothly.</p>
    <p class="service__text">With a free appraisal and efficient repair, you can feel secure knowing that the job will be done right the first time!</p>
    <span class="btn btn--blue">Read More</span>
  </div>
  <div class="service__photo" role="img" aria-label="Couple checking the engine of a convertible on a grassy roadside" style="background:linear-gradient(180deg,#6f8f4a 0%,#3c3f3a 50%,#8aa55a 100%)"></div>
</article>

<article class="service" style="top:537px;height:160px">
  <div class="service__body">
    <h2 class="service__title">Have a classic car that needs specialist engine work?</h2>
    <p class="service__text">Have a classic car engine reconditioned or get maximum speed &amp; performance for your car.</p>
    <p class="service__text">If you would like your vehicle to have more of a kick, you can bring your race car or classic car to us to have the engine restored or to have a complete overhaul to maximise performance.</p>
    <span class="btn btn--blue">Read More</span>
  </div>
  <div class="service__photo" role="img" aria-label="Classic car dashboard gauges" style="background:radial-gradient(circle at 55% 45%,#9a9a96 0%,#3a3a38 55%,#151515 100%)"></div>
</article>

<article class="service" style="top:721px;height:160px">
  <div class="service__body">
    <h2 class="service__title">Own a race car that needs specialist engine repairs?</h2>
    <p class="service__text">Have a classic car engine reconditioned or get maximum speed &amp; performance for your car.</p>
    <p class="service__text">If you would like your vehicle to have more of a kick, you can bring your race car or classic car to us to have the engine restored or to have a complete overhaul to maximise performance.</p>
    <span class="btn btn--blue">Read More</span>
  </div>
  <div class="service__photo" role="img" aria-label="Pit crew working on a red race car" style="background:linear-gradient(180deg,#4a7bc4 0%,#3a4f8a 40%,#c8352a 75%,#d8a030 100%)"></div>
</article>

<article class="service" style="top:905px;height:155px">
  <div class="service__body">
    <h2 class="service__title">Are you a garage owner, needing to outsource an engine machining job from one of your customers?</h2>
    <p class="service__text">We have the tools to offer you all of the services needed to ensure your customers engine is running smoothly.</p>
    <p class="service__text">From single cylinder engines to heavy diesel engines, we can handle all machining jobs.</p>
    <span class="btn btn--blue">Read More</span>
  </div>
  <div class="service__photo" role="img" aria-label="Golden engine oil pouring into a filler opening" style="background:radial-gradient(ellipse at 50% 70%,#b08a2a 0%,#4a3a1a 35%,#0c0c0c 70%)"></div>
</article>

<aside class="sidebar">
  <div class="cta cta--dark" style="height:155px">
    <h3 class="cta__title">Need service and repair for a private vehicle?</h3>
    <p class="cta__text">Get an efficient and honest diagnosis, along with repair work that will have your car running smoothly.</p>
    <span class="btn btn--gold">Make an Enquiry</span>
  </div>
  <div class="cta cta--blue" style="height:155px">
    <h3 class="cta__title">Interested in becoming a trade customer?</h3>
    <p class="cta__text">You can outsource your the specialist machining jobs to us at very competitive rates.</p>
    <span class="btn btn--white">Make an Enquiry</span>
  </div>
  <div class="cta cta--dark" style="height:163px">
    <h3 class="cta__title">Is your classic or race car your passion?</h3>
    <p class="cta__text">Is your vintage car just sitting in your garage? Contact us to get the engine on your classic car or race car repaired or overhauled.</p>
    <span class="btn btn--gold">Make an Enquiry</span>
  </div>
</aside>

<section class="partners">
  <span class="partners__badge-a" role="img" aria-label="Member association badge"></span>
  <p class="partners__text-a">As members of the NZMRG, you can rely on us to get the job done right, first time!</p>
  <span class="partners__badge-b" role="img" aria-label="Stockist badge"></span>
  <p class="partners__text-b">Official stockists of Southern Head Supply</p>
</section>

<footer class="site-footer">© Harlow Brandt Engine Reconditioners, 2014</footer>
</body>
</html>
```